Dr Colin Pemberly needs a logo for letter head and business cards

I need a logo design for my stationery (letter head & business card). I am a Respiratory and Sleep medicine doctor who treats adults.
I treat asthma, snoring and other breathing problems and the symbols could include something relating to this. examples: ZZZ or a bed etc for snoring/sleep, a symbol of lungs , or other option. The blue lung could include a small red circle in the left one to indicate lung cancer.

Ideally in blue or green colour with maybe a small amount of red to indicate illness in the lung or somehow related to sleep.

the second side of the business card could include the text below:

Your next appointment is:
On ________________at_______________AM/PM

Please call to reschedule if necessary.

Target Market(s)

Middle aged to elderly patients and other medical staff. Professional context.

Industry/Entity Type

Medical

Contact Information for Business Card

Dr Colin Pemberly
MBBS (hons),
FRACP (Sleep & Respiratory).
DTM&H, MHSM, GC-CU.
www.harwoodclinicians.example

Locations:
Kestrel Private Specialist Consulting Rooms,
Level1, 517 Durnford Road,
Oakmere VIC 3187
Ph: 9461 7053
Fax: 8315 6640

Logo Text

that this is a respectable and trustworthy medical specialist

Font styles to use
Sans Serif

Colors
34a6d7
0655a3
33b8a4
00a88f
85cae6
ec1f27

Requirements
Must have
• my name in the logo . I have included my current business card and need to replace the logo/wording in the top right corner "Kestrel Private specialist Consulting Rooms" for my own personalised logo.
Nice to have
• symbol relating to lungs /breathing and sleep
Should not have
• Should not have the location in the logo of the business card

```html
<!DOCTYPE html>
<html lang="en">
<head>
<meta charset="utf-8">
<title>Dr Colin Pemberly – Stationery</title>
<link rel="stylesheet" href="https://fonts.googleapis.com/css2?family=Roboto:wght@400;500;700&display=swap">
<style>
  :root {
    --green: #8cc63f;
    --blue: #3563a0;
    --blue-deep: #2f5d98;
    --sky: #a9d9e6;
    --ink: #4a4a4a;
    --paper: #ffffff;
    --stage: #eceef1;
  }
  * { box-sizing: border-box; margin: 0; padding: 0; }
  html, body { width: 1200px; height: 1200px; overflow: hidden; }
  body {
    position: relative;
    background: var(--stage);
    font-family: "Roboto", Arial, sans-serif;
    color: var(--ink);
  }

  /* ---------- business card: appointment side ---------- */
  .card {
    position: absolute;
    width: 500px;
    height: 286px;
    box-shadow: 0 4px 14px rgba(0,0,0,.12);
    overflow: hidden;
  }
  .card-back {
    left: 60px; top: 60px;
    background: var(--sky);
    color: var(--paper);
    padding: 34px 40px;
    font-size: 14px;
  }
  .card-back .appt-label { margin-bottom: 26px; }
  .card-back .appt-line { display: flex; align-items: flex-end; gap: 6px; }
  .card-back .blank { flex: 1; border-bottom: 1px solid var(--paper); height: 14px; }
  .card-back .blank.short { flex: .8; }
  .card-back .reschedule { position: absolute; left: 40px; right: 40px; bottom: 32px; text-align: center; }

  /* ---------- business card: contact side ---------- */
  .card-front { left: 60px; top: 376px; background: var(--paper); }
  .card-front .tab {
    position: absolute; left: 0; top: 22px;
    width: 8px; height: 38px; background: var(--blue);
    border-radius: 0 6px 6px 0;
  }
  .card-front .holder { position: absolute; left: 28px; top: 22px; }
  .card-front .holder-name { color: var(--green); font-weight: 700; font-size: 20px; }
  .card-front .credentials { color: var(--blue); font-size: 12.5px; line-height: 1.35; margin-top: 4px; }
  .card-front .contact { position: absolute; left: 28px; top: 170px; color: var(--blue); font-size: 12.5px; line-height: 1.4; }
  .contact-row { display: flex; align-items: center; gap: 6px; }
  .contact-row svg { width: 10px; height: 10px; fill: var(--green); }
  .card-front .address { margin-bottom: 6px; }
  .card-front .mark {
    position: absolute; right: 28px; top: 150px;
    display: flex; align-items: center; gap: 10px;
  }

  /* ---------- shared name mark ---------- */
  .mark-dot { width: 14px; height: 14px; border-radius: 50%; background: var(--green); flex: none; }
  .mark-name { font-weight: 700; color: var(--blue); font-size: 17px; white-space: nowrap; }

  /* ---------- letterhead ---------- */
  .letterhead {
    position: absolute; left: 640px; top: 60px;
    width: 430px; height: 600px;
    background: var(--paper);
    box-shadow: 0 4px 14px rgba(0,0,0,.12);
    overflow: hidden;
    font-size: 9px;
    line-height: 1.5;
  }
  .letterhead .edge-blue { position: absolute; right: 0; top: 0; bottom: 0; width: 12px; background: var(--blue); }
  .letterhead .edge-green { position: absolute; right: 16px; top: 0; bottom: 0; width: 6px; background: var(--green); }
  .letterhead .head-mark { position: absolute; left: 36px; top: 34px; display: flex; align-items: center; gap: 8px; }
  .letterhead .head-mark .mark-name { color: var(--green); font-size: 14px; }
  .letterhead .head-mark .mark-dot { width: 10px; height: 10px; }
  .letterhead .head-contact { position: absolute; right: 40px; top: 30px; text-align: right; color: var(--ink); font-size: 8px; }
  .letterhead .letter { position: absolute; left: 36px; right: 56px; top: 96px; }
  .letterhead .letter p { margin-bottom: 12px; }
  .letterhead .signer { margin-top: 20px; }

  /* ---------- presentation folder ---------- */
  .folder {
    position: absolute; left: 60px; top: 700px;
    width: 1080px; height: 450px;
    display: flex;
    box-shadow: 0 10px 24px rgba(0,0,0,.18);
  }
  .folder-panel { position: relative; width: 50%; height: 100%; overflow: hidden; }
  .folder-inside { background: var(--paper); }
  .folder-cover { background: var(--blue-deep); }
  .folder-inside .inside-mark { position: absolute; left: 0; right: 0; top: 338px; text-align: center; }
  .folder-inside .inside-mark .row { display: inline-flex; align-items: center; gap: 8px; }
  .tagline { font-weight: 700; color: var(--blue); font-size: 10px; letter-spacing: 1.5px; margin-top: 3px; }
  .folder-cover .cover-mark { position: absolute; right: 40px; top: 70px; text-align: center; }
  .folder-cover .cover-mark .row { display: inline-flex; align-items: center; gap: 8px; }
  .folder-cover .mark-name, .folder-cover .tagline { color: var(--paper); }
  .folder-cover .mark-dot { background: var(--paper); }
</style>
</head>
<body>

  <!-- Business card, appointment side -->
  <section class="card card-back">
    <p class="appt-label">Your next appointment is:</p>
    <div class="appt-line">
      <span>On</span><span class="blank"></span>
      <span>at</span><span class="blank short"></span>
      <span>am/pm</span>
    </div>
    <p class="reschedule">Please call 9461 7053 to reschedule or cancel your appointment</p>
  </section>

  <!-- Business card, contact side -->
  <section class="card card-front">
    <span class="tab"></span>
    <div class="holder">
      <h1 class="holder-name">Dr. Colin Pemberly</h1>
      <p class="credentials">MBBS (Hon),<br>FRACP (Sleep &amp; Respiratory),<br>DTM&amp;H, MHSM, GC-CU.</p>
    </div>
    <div class="contact">
      <p class="address">517 Durnford Road,<br>Oakmere VIC 3187</p>
      <p class="contact-row">
        <svg viewBox="0 0 10 10"><path d="M2 0.5 L3.6 2.6 L2.8 3.6 Q4 6 6.4 7.2 L7.4 6.4 L9.5 8 L8.3 9.5 Q4.5 9.2 2 6.8 Q0.2 4.6 0.5 1.7 Z"/></svg>
        9461 7053
      </p>
      <p class="contact-row">
        <svg viewBox="0 0 10 10"><rect x="2.5" y="0.5" width="5" height="3"/><rect x="0.5" y="3.5" width="9" height="4" rx="1"/><rect x="2.5" y="6.5" width="5" height="3"/></svg>
        8315 6640
      </p>
      <p class="contact-row">
        <svg viewBox="0 0 10 10"><circle cx="5" cy="5" r="4.5"/></svg>
        www.harwoodclinicians.example
      </p>
    </div>
    <div class="mark">
      <span class="mark-dot"></span>
      <span class="mark-name">Dr Colin Pemberly</span>
    </div>
  </section>

  <!-- Letterhead -->
  <section class="letterhead">
    <span class="edge-green"></span>
    <span class="edge-blue"></span>
    <div class="head-mark">
      <span class="mark-dot"></span>
      <span class="mark-name">Dr Colin Pemberly</span>
    </div>
    <div class="head-contact">
      <p>9461 7053</p>
      <p>8315 6640</p>
    </div>
    <div class="letter">
      <p>The Practice Manager<br>Oakmere Health Group<br>28 / 07 / 2024</p>
      <p>Dear Sir / Madam</p>
      <p>Thank you for referring your patient to our rooms. We reviewed the recent sleep study and lung function results in detail today.</p>
      <p>The findings suggest moderate obstructive sleep apnoea. We recommend a trial of nightly therapy with review in six weeks.</p>
      <p>Please contact the rooms if you have any questions about this plan.</p>
      <p class="signer">Sincerely,<br><br>Dr Colin Pemberly</p>
    </div>
  </section>

  <!-- Presentation folder -->
  <section class="folder">
    <div class="folder-panel folder-inside">
      <div class="inside-mark">
        <div class="row">
          <span class="mark-dot"></span>
          <span class="mark-name">Dr Colin Pemberly</span>
        </div>
        <p class="tagline">Specialist Consulting Rooms</p>
      </div>
    </div>
    <div class="folder-panel folder-cover">
      <div class="cover-mark">
        <div class="row">
          <span class="mark-dot"></span>
          <span class="mark-name">Dr Colin Pemberly</span>
        </div>
        <p class="tagline">Specialist Consulting Rooms</p>
      </div>
    </div>
  </section>

</body>
</html>
```